Quellbyte Business cards template

We're looking for something modern and elegant. We are a reseller of technology (computers, datacenter, etc). Color theme would be "only" white with the incorporation of the blue that's present on our website (Quellbyte.com) and logo file. We would like for the card to provide all the necessary info for the specific person (Phone#, fax#, email, name, website URL) . I'm attaching the logo file to this request. Please have it show Lakemont/Fairbridge somewhere, without providing specific addresses.

Target Market(s)

All b2b

Industry/Entity Type

Business

Contact Information for Business Card

Please have the color scheme be represented by only the white and blue from our website (Quellbyte.com) and logo. We would like to logo on the card, but not big and overwhelming. This card will be used as a template for anybody within the company, it should display the user's name, phone#, fax#, email, job title and website URL. Please have it show Lakemont/Fairbridge somewhere, without providing our specific addresses. Really, we're looking for a clean, simple and elegant look.

Font styles to use
Serif

Requirements
Must have
• Please see card details
Nice to have
• Please see card details
Should not have
• Anything tacky or tagline.

```html
<!DOCTYPE html>
<html lang="en">
<head>
<meta charset="UTF-8">
<title>Quellbyte Business Cards</title>
<link rel="stylesheet" href="https://fonts.googleapis.com/css2?family=Roboto:wght@400;500&family=Roboto+Condensed:wght@500;700&display=swap">
<style>
  :root {
    --backdrop: #3b3c3f;
    --card: #2a2b2e;
    --card-edge: #232427;
    --brand-blue: #1a95dd;
    --text-white: #f2f2f2;
    --divider: #8a8b8e;
  }
  * { box-sizing: border-box; margin: 0; padding: 0; }
  html, body {
    width: 1200px; height: 900px; overflow: hidden;
    background: var(--backdrop);
    font-family: "Roboto", Arial, sans-serif;
  }
  .canvas { position: relative; width: 1200px; height: 900px; }
  .card {
    position: absolute; left: 250px; width: 700px; height: 400px;
    background: var(--card);
    border: 1px solid var(--card-edge);
    box-shadow: 0 10px 30px rgba(0,0,0,0.45);
  }
  .card-front { top: 40px; }
  .card-back { top: 460px; }

  /* front */
  .brand-name {
    position: absolute; top: 118px; left: 0; width: 100%;
    text-align: center;
    font-family: "Roboto", Arial, sans-serif;
    font-weight: 500; font-size: 76px; line-height: 1.1; letter-spacing: 1px;
    color: var(--brand-blue);
  }
  .front-url {
    position: absolute; top: 262px; left: 0; width: 100%;
    text-align: center; font-size: 16px; letter-spacing: 5px;
    color: var(--text-white);
  }

  /* back */
  .identity {
    position: absolute; top: 150px; right: 330px;
    text-align: right;
    font-family: "Roboto Condensed", "Arial Narrow", sans-serif;
    color: var(--brand-blue);
  }
  .person-name { font-size: 34px; font-weight: 700; line-height: 1; }
  .person-title { font-size: 18px; font-weight: 500; margin-top: 8px; letter-spacing: .5px; }
  .divider {
    position: absolute; left: 392px; top: 140px; width: 2px; height: 110px;
    background: linear-gradient(to bottom, transparent, var(--divider), transparent);
    transform: rotate(6deg);
  }
  .contact-list {
    position: absolute; top: 148px; left: 418px; list-style: none;
    color: var(--text-white); font-size: 17px; font-weight: 500;
  }
  .contact-list li { display: flex; align-items: center; gap: 10px; height: 24px; }
  .contact-list svg, .location svg { flex: none; fill: var(--brand-blue); }
  .location {
    position: absolute; top: 318px; left: 0; width: 100%;
    display: flex; justify-content: center; align-items: center; gap: 8px;
    color: var(--text-white); font-size: 17px; font-weight: 500;
  }
</style>
</head>
<body>
<main class="canvas">
  <section class="card card-front">
    <div class="brand-name">Quellbyte</div>
    <div class="front-url">www.quellbyte.com</div>
  </section>

  <section class="card card-back">
    <div class="identity">
      <div class="person-name">AVERY LANE</div>
      <div class="person-title">CEO/FOUNDER</div>
    </div>
    <div class="divider"></div>
    <ul class="contact-list">
      <li>
        <svg width="14" height="14" viewBox="0 0 24 24"><path d="M6.6 10.8a15.1 15.1 0 0 0 6.6 6.6l2.2-2.2a1 1 0 0 1 1-.25 11.4 11.4 0 0 0 3.6.57 1 1 0 0 1 1 1V20a1 1 0 0 1-1 1A17 17 0 0 1 3 4a1 1 0 0 1 1-1h3.5a1 1 0 0 1 1 1c0 1.25.2 2.45.57 3.57a1 1 0 0 1-.25 1z"/></svg>
        <span>1-855-555-QUEL (7835)</span>
      </li>
      <li>
        <svg width="14" height="14" viewBox="0 0 24 24"><path d="M6 2h12v6H6zM3 9h18a1 1 0 0 1 1 1v7h-4v5H6v-5H2v-7a1 1 0 0 1 1-1zm5 6v5h8v-5z"/></svg>
        <span>482 555 0193</span>
      </li>
      <li>
        <svg width="14" height="14" viewBox="0 0 24 24"><path d="M2 5h20v14H2zm2 2v.5l8 5 8-5V7l-8 5z"/></svg>
        <span>info@quellbyte.com</span>
      </li>
      <li>
        <svg width="14" height="14" viewBox="0 0 24 24"><path d="M12 2a10 10 0 1 0 0 20 10 10 0 0 0 0-20zm-1 17.9A8 8 0 0 1 4.1 11H7c.1 2.7.8 5.6 4 8.9zM4.1 9A8 8 0 0 1 11 4.1C8 7 7.2 8 7 9zm8.9 10.9c3.2-3.3 3.9-6.2 4-8.9h2.9a8 8 0 0 1-6.9 8.9zM17 9c-.2-1-1-2-4-4.9A8 8 0 0 1 19.9 9zM9 11h6c-.1 2.3-.9 4.6-3 7-2.1-2.4-2.9-4.7-3-7zm0-2c.2-1 1-2.7 3-4.8 2 2.1 2.8 3.8 3 4.8z"/></svg>
        <span>www.quellbyte.com</span>
      </li>
    </ul>
    <div class="location">
      <svg width="14" height="18" viewBox="0 0 24 30"><path d="M12 0a10 10 0 0 0-10 10c0 7.5 10 20 10 20s10-12.5 10-20A10 10 0 0 0 12 0zm0 14a4 4 0 1 1 0-8 4 4 0 0 1 0 8z"/></svg>
      <span>Lakemont/Fairbridge</span>
    </div>
  </section>
</main>
</body>
</html>
```